Brindlewick Music Studio needs a promotional postcard design

We are looking for a postcard design for a small business that provides clients with private music lesson instruction. We are looking for a design that will convey the message of "music is fun for kids" that will appeal to parents and encourage them to sign up. We have a company logo that should be used and our color scheme is teal and turquoise. All of our contact info should be displayed as well.

Target Market(s)

Parents with young kids

Contact Information for Business Card

web: www.brindlewickmusicstudio.example
email: lessons@brindlewickmusicstudio.example
phone: 202-555-0147

Font styles to use
Serif
Sans Serif

Colors
33b8a4
86cfc6
0456a4
87cfc6

Requirements
Must have
• Music lessons in your home
• Creating little stars one at a time
• Sign Up Now
• Please use these images:
Nice to have
• Something like this sample postcard:

```html
<!DOCTYPE html>
<html lang="en">
<head>
<meta charset="utf-8">
<title>Brindlewick Music Studio – Music Is Fun For Kids</title>
<link rel="stylesheet" href="https://fonts.googleapis.com/css2?family=Lora:ital,wght@0,400;1,400&family=Roboto+Condensed:wght@400;700&display=swap">
<style>
  :root {
    --teal: #52bbbd;
    --turquoise-light: #a5d5d7;
    --headline: #c9e6e6;
    --white: #ffffff;
    --deep-blue: #0456a4;
  }
  html, body {
    margin: 0;
    padding: 0;
    width: 1200px;
    height: 686px;
    overflow: hidden;
  }
  .postcard {
    position: relative;
    width: 1200px;
    height: 686px;
    background: var(--teal);
    overflow: hidden;
    font-family: "Roboto Condensed", "Arial Narrow", sans-serif;
  }
  .side-art {
    position: absolute;
    top: 0;
    right: 0;
    width: 230px;
    height: 686px;
    background: linear-gradient(180deg, var(--turquoise-light), #b6dedf);
  }
  .content {
    position: absolute;
    left: 0;
    top: 0;
    width: 970px;
    height: 560px;
    display: flex;
    flex-direction: column;
    align-items: center;
    text-align: center;
    color: var(--white);
  }
  .studio-mark {
    margin-top: 96px;
    display: flex;
    align-items: center;
    gap: 16px;
    white-space: nowrap;
  }
  .studio-mark__dot {
    width: 22px;
    height: 22px;
    border-radius: 50%;
    background: var(--white);
  }
  .studio-mark__name {
    margin: 0;
    font-size: 40px;
    font-weight: 700;
    letter-spacing: 1px;
  }
  .tagline {
    margin: 34px 0 0;
    font-family: "Lora", Georgia, serif;
    font-size: 30px;
    line-height: 1.35;
  }
  .tagline--sub {
    margin-top: 4px;
    font-style: italic;
    font-size: 24px;
  }
  .sign-up {
    margin-top: 30px;
    padding: 12px 40px;
    background: var(--white);
    color: var(--deep-blue);
    border-radius: 30px;
    font-size: 26px;
    font-weight: 700;
    letter-spacing: 2px;
    text-transform: uppercase;
  }
  .contact {
    margin: 30px 0 0;
    padding: 0;
    list-style: none;
    display: flex;
    gap: 28px;
    font-size: 19px;
    white-space: nowrap;
  }
  .headline {
    position: absolute;
    left: 38px;
    bottom: 26px;
    margin: 0;
    color: var(--headline);
    font-size: 82px;
    font-weight: 700;
    line-height: 1;
    letter-spacing: 1px;
    text-transform: uppercase;
    white-space: nowrap;
  }
</style>
</head>
<body>
  <main class="postcard">
    <div class="side-art" role="img" aria-label="Illustration of a guitar body in light turquoise"></div>

    <section class="content">
      <div class="studio-mark">
        <span class="studio-mark__dot"></span>
        <p class="studio-mark__name">Brindlewick Music Studio</p>
      </div>
      <p class="tagline">Music lessons in your home</p>
      <p class="tagline tagline--sub">Creating little stars one at a time</p>
      <span class="sign-up">Sign Up Now</span>
      <ul class="contact">
        <li>www.brindlewickmusicstudio.example</li>
        <li>lessons@brindlewickmusicstudio.example</li>
        <li>202-555-0147</li>
      </ul>
    </section>

    <h1 class="headline">Music is fun for kids</h1>
  </main>
</body>
</html>
```